依頼概要
■依頼の概要
婚活男子に向けた電子書籍(pagelo出版)の表紙デザイン作成をお願いします。
電子書籍なので、タイトルがはっきり分かるものでお願いします。

■本の内容
婚活中の男性が、婚活成幸するための方法や事例を書いています。
婚活男子に、勇気・元気・やる気と知識を与える内容となっています。
原稿内容を添付します。

■読者ターゲット
文字通り、婚活がうまくいかない男性全般
(・無口でおしゃべりが続かない・女性のことがサッパリ分からない・いい加減、婚活を卒業したい・草食系男子etc…と言ったところでしょうか)

■デザイン要望
原稿内容を参考にしていただいて、より売れることを目的としたデザインにしてください。
デザイナーさんのパフォーマンスを引き出したいので、デザイナーさんのセンスにお任せします。
また、下記の内容にもご注意ください。

■お願い&ご相談
今回は男性版ですが、同じシリーズで女性版も(できれば2ヶ月以内に)出したいと思っています。
それでできれば、「色違い」「類似デザイン」(多少の文字変更有り)で、同シリーズとして認知してもらえるような、デザインを希望しています。
尚、女性版の際に文字やデザインを修正していただく場合、対応可能かと、その場合の追加料金についても合わせてお知らせください。

■その他
Tasqoraの利用含め初めての経験で私自身分からないことばかりですが、何かご不明な点がございましたら、お気軽にご質問ください。
■タイトル&サブキャッチ
タイトル:縁探しに迷っている男子に贈る一冊
サブキャッチ:~会話・外見・条件に自信がなくても結婚できる~

■著者
良縁づくりナビゲーター 柊 あき(ひいらぎ あき)
肩書(良縁づくりナビゲーター)と読み仮名を入れる・入れないはデザイナーさんの感性にお任せします。
尚、読み仮名を入れる場合、上記のように()書きにするか、紡の上にルビを振るかも含めてお任せします。
■読者プレゼント
『惹かれる人』に変わる魔法の言い回し
ご提案をいただけて、さすがプロのデザイナーさんはセンスが違うな~と感心しております(*^-^*)
まだまだいろんな切り口のデザインを考えていただき、ご提案いただけましたら有難く嬉しく思います。
また私はデザインの素人で何も分かりませんが、デザインだけでなく添付ファイル原稿(1時間で読めます)の中から読者に響く文言を拾っていただいて入れていただいても嬉しく思います。

Tasqora 初めての利用で分からないことばかりですが、デザイナーさんはデザインだけでなくご対応にもプロ意識がみえてとても嬉しく思っております(^o^)
引き続きご提案を募集させていただきますので、皆様ご提案の程どうぞ宜しくお願い申し上げますm(__)m
最初に予定していた日にちには他の準備が間に合わなくなりましたので、せっかくなので締切日を1日延ばしました。
引き続きステキなご提案をいただけましたら嬉しい限りです。
デザイナーの皆様、何卒よろしくお願い致しますm(__)m
デザイナーの皆様、たくさんご提案をいただきまして本当にありがとうございます。
お一人お一人にお礼の言葉をお贈りしたいのですが、今日は締切日だからかいつもになくたくさんご提案をいただいて、コメントが間に合いません。
ですので、ここでまとめてお礼の言葉をお贈りさせていただきたいと思います。
どれもプロの皆様のお仕事はステキなものばかりで、ここ何日もどれにしようか・・・悩み続けておりました。
正直、私一人では決めかねてますので、他の方のご意見も伺ってから決めさせていただこうと考えております。
IT超苦手でTasqora初めての利用の私です。
正直まだ利用方法すら理解していない状況ですが、皆様のお気持ちが有難くって有難くって、もう本当に感謝しかありません。
本当にほんとうにありがとうございますm(__)m
しかし、利用方法をあまり理解しておりませんので、今までに失礼なことがあったようでしたら謝らせていただきます。申し訳ございませんm(__)m
この度は、皆様本当にありがとうございました!

20名弱ほどの方々に表紙デザイン選挙・投票をいただいて決めさせていただきました。
その結果、ぶっちぎりの断トツ1位であったため決めさせていただきました。
こちらのデザイナー様は、私の原稿をよくお読みいただいているな~と感じました。
その意を汲んでいただいたものが表紙に表れていると思います。
事前にお知らせしたタイトルや名前・読者プレゼント以外にも原稿を読んでいただいたからこそ分かるキャッチ―な文言を取り入れてくださり、それにあったデザインに仕上がっていると思っております。

この度は、皆様からたくさんのご提案をいただきありがとうございました。
ステキなご提案をたくさんいただけて私一人では決められずにおりましたので、まず、スピリチュアルの方に一つずつ見ていただき1つ1つ解説をいただきました。
そのうえである程度「良し」とされたものの中から、20人弱の方々に投票を行っていただいて決めさせていただきました。
本来ならお一人お一人にお礼の言葉をお贈りさせていただかなければならないのだと思いますが、この場を借りて心から感謝&お礼を申し上げます。
本当にありがとうございました。

```html
<!DOCTYPE html>
<html lang="ja">
<head>
<meta charset="utf-8">
<title>縁探しに迷っている男子に贈る一冊</title>
<link href="https://fonts.googleapis.com/css2?family=M+PLUS+1p:wght@500;700;800;900&family=Noto+Serif+JP:wght@600;700&display=swap" rel="stylesheet">
<style>
  :root {
    --blue-deep: #155fb3;
    --blue: #1f74cc;
    --blue-light: #3b8fdc;
    --white: #ffffff;
    --ink: #1e1e1e;
    --gold: #8a6526;
    --cream: #fbf4e4;
    --cream-edge: #e9d6a8;
    --photo-light: #f3ede6;
    --photo-mid: #d9cfc6;
    --photo-dark: #9f9a96;
  }
  * { margin: 0; padding: 0; box-sizing: border-box; }
  html, body { width: 750px; height: 1200px; overflow: hidden; background: #fff; }
  .cover {
    position: relative; width: 750px; height: 1200px; overflow: hidden;
    font-family: "M PLUS 1p", sans-serif;
  }
  .title-band {
    position: absolute; left: 0; top: 0; width: 750px; height: 512px;
    background: linear-gradient(180deg, var(--blue-light) 0%, var(--blue) 45%, var(--blue-deep) 100%);
  }
  .heart { position: absolute; left: 18px; top: -10px; width: 190px; height: 160px; }
  .author { position: absolute; right: 26px; top: 20px; text-align: center; color: var(--white); }
  .author-role { font-size: 17px; font-weight: 700; letter-spacing: 1px; }
  .author-name { font-size: 36px; font-weight: 800; letter-spacing: 6px; line-height: 1.25; }
  .author-roman { font-size: 15px; font-weight: 500; letter-spacing: 1px; }
  .title {
    position: absolute; color: var(--white);
    font-weight: 900; line-height: 1; white-space: nowrap;
    text-shadow: 0 3px 6px rgba(0, 40, 90, 0.35);
  }
  .title-line-1 { left: 118px; top: 66px; font-size: 108px; }
  .title-line-1 .title-small { font-size: 66px; }
  .title-line-2 { left: 0; width: 750px; text-align: center; top: 226px; font-size: 98px; }
  .title-line-3 { left: 0; width: 750px; text-align: center; top: 370px; font-size: 94px; }
  .photo {
    position: absolute; left: 0; top: 512px; width: 750px; height: 688px;
    background: linear-gradient(100deg, var(--photo-dark) 0%, var(--photo-mid) 30%, var(--photo-light) 60%, var(--photo-mid) 100%);
  }
  .gift-badge {
    position: absolute; left: 58px; top: 768px; width: 236px; height: 236px; border-radius: 50%;
    background: radial-gradient(circle at 40% 35%, #fffaf0 0%, var(--cream) 60%, var(--cream-edge) 100%);
    box-shadow: 0 4px 14px rgba(0,0,0,0.2);
    text-align: center; color: var(--gold); font-family: "Noto Serif JP", serif; font-weight: 700;
  }
  .gift-label {
    display: inline-block; margin-top: 26px; padding: 4px 14px; border-radius: 20px;
    background: var(--gold); color: var(--cream); font-size: 21px; transform: rotate(-8deg);
  }
  .gift-text { margin-top: 10px; font-size: 26px; line-height: 1.3; }
  .gift-text .gift-key { font-size: 30px; }
  .catch-band {
    position: absolute; left: 0; top: 990px; width: 750px; height: 210px;
    background: rgba(255,255,255,0.9);
  }
  .catch { position: absolute; right: 22px; font-weight: 900; color: var(--ink); white-space: nowrap; line-height: 1; }
  .catch-line-1 { top: 1025px; font-size: 64px; }
  .catch-line-2 { top: 1108px; font-size: 58px; }
  .catch-accent { color: var(--blue); }
</style>
</head>
<body>
<div class="cover">
  <div class="title-band">
    <svg class="heart" viewBox="0 0 190 160" aria-hidden="true">
      <path d="M95 150 C40 110 8 80 8 45 C8 18 28 2 52 2 C72 2 86 14 95 32 C104 14 118 2 138 2 C162 2 182 18 182 45 C182 80 150 110 95 150 Z"
            fill="rgba(255,255,255,0.12)" stroke="rgba(255,255,255,0.55)" stroke-width="5"/>
    </svg>
    <div class="author">
      <p class="author-role">良縁づくりナビゲーター</p>
      <p class="author-name">柊 あき</p>
      <p class="author-roman">Hiiragi Aki</p>
    </div>
    <h1>
      <span class="title title-line-1">縁探し<span class="title-small">に</span></span>
      <span class="title title-line-2">迷っている</span>
      <span class="title title-line-3">男子に贈る一冊</span>
    </h1>
  </div>

  <div class="photo" role="img" aria-label="白いドレスの花嫁がブーケを持ち、手前に新郎の後ろ姿が見える結婚式の写真"></div>

  <div class="gift-badge">
    <span class="gift-label">読者プレゼント</span>
    <p class="gift-text"><span class="gift-key">『惹かれる人』</span><br>に変わる<br>魔法の言い回し</p>
  </div>

  <div class="catch-band"></div>
  <p class="catch catch-line-1">会話・外見・条件に</p>
  <p class="catch catch-line-2">自信がなくても<span class="catch-accent">結婚できる</span></p>
</div>
</body>
</html>
```